Automotive spring company needs banner for website

Banner dimensions: 3840 x 880 pixels
Banner need to be consistent with our branding (logo, stationary, colors, fonts, message).
People images should show happiness and it is preferable those people are in or around a car unless it ties into one of the 3 quotes in the must haves below.
Use color blue #4885ed
and gold color #f7d105
Minimal, strong, clean, & tech

Target Market(s)

35-55 male and female

Industry/Entity Type

Auto Repair

Requirements
Must have
• Clickable element for "Shop" or "Make an Appointment"
• "25 Years of Customer Satisfaction" or
• "Get it Done Right by Specialist" or
• "Peace of Mind National Warranty"
• Use our font, Eurostile and/or complimentary font paring

```html
<!DOCTYPE html>
<html lang="en">
<head>
<meta charset="utf-8">
<title>Coilmark – Website Banners</title>
<link rel="stylesheet" href="https://fonts.googleapis.com/css2?family=Archivo:wght@700;800;900&family=Michroma&display=swap">
<style>
  :root {
    --brand-blue: #4885ed;
    --brand-gold: #f7d105;
    --ink: #111111;
    --backdrop: #000000;
  }
  * { margin: 0; padding: 0; box-sizing: border-box; }
  html, body { width: 1200px; height: 1200px; overflow: hidden; background: var(--backdrop); }
  .canvas { position: relative; width: 1200px; height: 1200px; }
  .banner { position: absolute; left: 14px; width: 1175px; height: 269px; overflow: hidden; }
  .banner--first { top: 313px; }
  .banner--second { top: 618px; }
  .banner__art { position: absolute; inset: 0; width: 1175px; height: 269px; }

  .tenure {
    position: absolute; left: 0; top: 269px;
    width: 269px; height: 104px;
    transform: rotate(-90deg); transform-origin: top left;
    display: flex; align-items: center; padding-left: 26px;
    font-family: "Archivo", sans-serif; color: var(--brand-gold);
  }
  .tenure__number { font-weight: 900; font-size: 84px; line-height: 1; letter-spacing: -2px; margin-right: 4px; }
  .tenure__words { display: flex; flex-direction: column; line-height: 0.9; }
  .tenure__years { font-weight: 800; font-size: 30px; }
  .tenure__caption { color: var(--brand-blue); font-weight: 700; font-size: 18px; display: none; }
  .tenure__line { font-weight: 700; font-size: 18px; color: #1b2d5a; }

  .pitch { position: absolute; right: 41px; top: 0; text-align: right; }
  .brand-name {
    position: absolute; right: 41px; top: 38px;
    font-family: "Michroma", sans-serif; font-size: 28px; letter-spacing: 1px;
    color: var(--brand-gold); white-space: nowrap;
  }
  .tagline {
    position: absolute; right: 41px; top: 114px;
    font-family: "Michroma", sans-serif; font-size: 17px; letter-spacing: 3px;
    color: #ffffff; white-space: nowrap;
  }
  .tagline__accent {
    position: absolute; right: 41px; top: 142px;
    font-family: "Michroma", sans-serif; font-size: 22px; letter-spacing: 5px;
    color: var(--brand-gold); white-space: nowrap;
  }
  .cta {
    position: absolute; left: 863px; top: 208px; width: 273px; height: 33px;
    background: var(--brand-gold); color: var(--ink);
    font-family: "Archivo", sans-serif; font-weight: 800; font-size: 14px; letter-spacing: 2.4px;
    display: flex; align-items: center; justify-content: center; text-decoration: none;
  }
</style>
</head>
<body>
<div class="canvas">

  <section class="banner banner--first">
    <svg class="banner__art" viewBox="0 0 1175 269" aria-hidden="false">
      <defs>
        <linearGradient id="photo-car" x1="0" y1="0" x2="1" y2="1">
          <stop offset="0" stop-color="#e9c93a"/>
          <stop offset="0.55" stop-color="#d8b530"/>
          <stop offset="1" stop-color="#3a3528"/>
        </linearGradient>
      </defs>
      <rect width="1175" height="269" fill="var(--brand-blue)"/>
      <rect x="104" width="14" height="269" fill="var(--brand-gold)"/>
      <polygon points="118,0 798,0 694,269 118,269" fill="var(--brand-gold)"/>
      <polygon role="img" aria-label="Photo: smiling woman standing beside a yellow compact car" points="118,0 782,0 678,269 118,269" fill="url(#photo-car)"/>
    </svg>
    <div class="tenure">
      <span class="tenure__number">25</span>
      <span class="tenure__words">
        <span class="tenure__years">years</span>
        <span class="tenure__line">of customer</span>
        <span class="tenure__line">satisfaction</span>
      </span>
    </div>
    <div class="brand-name">COILMARK</div>
    <div class="tagline">Get it Done Right by</div>
    <div class="tagline__accent">SPECIALIST</div>
    <a class="cta" href="#appointment">MAKE AN APPOINTMENT</a>
  </section>

  <section class="banner banner--second">
    <svg class="banner__art" viewBox="0 0 1175 269">
      <defs>
        <linearGradient id="photo-convertible" x1="0" y1="0" x2="1" y2="1">
          <stop offset="0" stop-color="#efe2cc"/>
          <stop offset="0.45" stop-color="#e8cf8a"/>
          <stop offset="1" stop-color="#8a7a55"/>
        </linearGradient>
      </defs>
      <rect width="1175" height="269" fill="var(--brand-blue)"/>
      <rect x="104" width="14" height="269" fill="var(--brand-gold)"/>
      <polygon points="118,0 798,0 694,269 118,269" fill="var(--brand-gold)"/>
      <polygon role="img" aria-label="Photo: woman in a yellow shirt with arms spread wide, standing in a convertible" points="118,0 782,0 678,269 118,269" fill="url(#photo-convertible)"/>
    </svg>
    <div class="tenure">
      <span class="tenure__number">25</span>
      <span class="tenure__words">
        <span class="tenure__years">years</span>
        <span class="tenure__line">of customer</span>
        <span class="tenure__line">satisfaction</span>
      </span>
    </div>
    <div class="brand-name">COILMARK</div>
    <div class="tagline">Get it Done Right by</div>
    <div class="tagline__accent">SPECIALIST</div>
    <a class="cta" href="#appointment">MAKE AN APPOINTMENT</a>
  </section>

</div>
</body>
</html>
```